Managed IT services business card design

We haven't needed a business card since the founding of the business in 2005. All our clients have been coming through word of mouth. And lately more and more existing clients are requesting for our business cards to pass on to their contacts in recommending us.
So we needing a business card design. We use various innovative solutions and methodologies to provide IT services to small businesses in managing their IT systems. Our role is the same as an in-house, full-time IT Manager for our clients, but outsourced. So we take care of all our clients' IT needs, just as an IT Manager would be expected to perform.
We have a holding website, which we're happy to leave for now. If we can use the same logo would be great - www.lomvex.com.au
Preferred colours are shades of are white, grey and black.
We pride our business with the following traits: proactive, good service, prompt response, trustworthy.
Target Market(s)
Small businesses of any industry
Industry/Entity Type
Business

```html
<!DOCTYPE html>
<html lang="en">
<head>
<meta charset="utf-8">
<title>Lomvex – Business Card</title>
<link rel="stylesheet" href="https://fonts.googleapis.com/css2?family=Open+Sans:ital,wght@0,300;0,400;0,700;1,400&display=swap">
<style>
  :root {
    --paper: #ffffff;
    --ink: #232829;
    --charcoal: #232829;
    --edge-black: #141718;
    --wave-light: #e9eced;
    --wave-mid: #c9d0d2;
    --on-dark: #ffffff;
  }
  * { margin: 0; padding: 0; box-sizing: border-box; }
  html, body {
    width: 1200px;
    height: 720px;
    overflow: hidden;
    background: var(--paper);
  }
  .card {
    position: relative;
    width: 1200px;
    height: 720px;
    background: var(--paper);
    font-family: "Open Sans", Arial, sans-serif;
    color: var(--ink);
    overflow: hidden;
  }
  .card-art {
    position: absolute;
    inset: 0;
    width: 1200px;
    height: 720px;
  }
  .tagline {
    position: absolute;
    left: 82px;
    top: 78px;
  }
  .tagline-title {
    font-weight: 700;
    font-size: 41px;
    line-height: 1.1;
    letter-spacing: 0.01em;
  }
  .tagline-since {
    font-weight: 300;
    font-size: 31px;
    line-height: 1.1;
    margin-left: 2px;
  }
  .website {
    position: absolute;
    left: 86px;
    top: 192px;
    font-size: 20px;
    font-weight: 400;
  }
  .brand {
    position: absolute;
    left: 836px;
    top: 62px;
    display: flex;
    align-items: center;
    gap: 34px;
  }
  .brand-name {
    font-weight: 300;
    font-size: 50px;
    letter-spacing: 0.22em;
    color: var(--ink);
  }
  .brand-mark {
    width: 22px;
    height: 22px;
    background: var(--ink);
  }
  .contact {
    position: absolute;
    left: 793px;
    top: 430px;
    color: var(--on-dark);
  }
  .contact-name {
    font-style: italic;
    font-weight: 400;
    font-size: 53px;
    line-height: 1.1;
  }
  .contact-role {
    font-style: italic;
    font-size: 21px;
    margin-top: 4px;
  }
  .contact-phone {
    display: flex;
    align-items: center;
    gap: 12px;
    margin-top: 34px;
    font-size: 21px;
  }
  .phone-icon { width: 19px; height: 19px; }
</style>
</head>
<body>
<main class="card">
  <svg class="card-art" viewBox="0 0 1200 720" aria-hidden="false">
    <defs>
      <linearGradient id="wave-fill" x1="0" y1="0" x2="1" y2="0">
        <stop offset="0" stop-color="var(--wave-mid)"/>
        <stop offset="0.5" stop-color="var(--wave-light)"/>
        <stop offset="1" stop-color="#f6f7f7"/>
      </linearGradient>
    </defs>
    <path class="wave-ribbon" role="img" aria-label="Flowing ribbon of fine grey lines"
          fill="url(#wave-fill)" opacity="0.75"
          d="M0 300 C 60 440, 150 520, 300 520 C 520 520, 700 380, 900 250 C 1000 190, 1120 210, 1200 290
             L1200 330 C 1100 250, 980 260, 860 330 C 650 450, 450 610, 250 700 C 150 720, 40 650, 0 560 Z"/>
    <path class="band-edge" fill="var(--edge-black)"
          d="M150 720 C 520 520, 800 300, 1030 292 C 1110 290, 1170 318, 1200 350 L1200 720 Z"/>
    <path class="band-fill" fill="var(--charcoal)"
          d="M280 720 C 600 540, 850 336, 1050 318 C 1120 314, 1170 338, 1200 366 L1200 720 Z"/>
  </svg>

  <header class="tagline">
    <h1 class="tagline-title">YOUR IT MANAGER</h1>
    <p class="tagline-since">SINCE 2005</p>
  </header>
  <p class="website">www.lomvex.com.au</p>

  <div class="brand">
    <span class="brand-name">lomvex</span>
    <span class="brand-mark" aria-hidden="true"></span>
  </div>

  <section class="contact">
    <h2 class="contact-name">YOUR NAME</h2>
    <p class="contact-role">Designation goes here</p>
    <p class="contact-phone">
      <svg class="phone-icon" viewBox="0 0 24 24" aria-hidden="true">
        <path fill="#ffffff" d="M6.6 10.8c1.4 2.8 3.8 5.1 6.6 6.6l2.2-2.2c.3-.3.7-.4 1-.2 1.1.4 2.3.6 3.6.6.6 0 1 .4 1 1V20c0 .6-.4 1-1 1C10.6 21 3 13.4 3 4c0-.6.4-1 1-1h3.5c.6 0 1 .4 1 1 0 1.3.2 2.5.6 3.6.1.3 0 .7-.2 1L6.6 10.8z"/>
      </svg>
      <span>+ 0987654321</span>
    </p>
  </section>
</main>
</body>
</html>
```